Templates for Construction Company

We are looking to have templates prepared for all aspects of our letter sending. Using our brand design. with similar layouts that look the same.

Letterheads design & Email signatures

We use letter heads for - quotes, contract correspondence, variations, formal letters, invitations

Target Market(s)

Clients documents sent in emails

Industry/Entity Type

Construction

Font styles to use
Serif
Sans Serif

Colors
0054AA
0677BA
7BADD7
CADEEF
E8F1F8

Requirements
Must have
• Easy to read, water marks on page
Nice to have
• Different options for different letters

```html
<!DOCTYPE html>
<html lang="en">
<head>
<meta charset="utf-8">
<title>Stonefield – Letterhead &amp; Email Signature</title>
<link rel="stylesheet" href="https://fonts.googleapis.com/css2?family=Montserrat:wght@400;500;600;700&family=Roboto:wght@400;500;700&display=swap">
<style>
  :root {
    --backdrop: #e5e3e4;
    --paper: #f0f0f0;
    --ink: #1b1b1b;
    --label: #555555;
    --brand-blue: #1f56a8;
    --brand-light: #5b8ccc;
    --band-dark: #1e1e1e;
    --watermark: rgba(91, 140, 204, 0.13);
  }
  * { margin: 0; padding: 0; box-sizing: border-box; }
  html, body { width: 1200px; height: 619px; overflow: hidden; }
  body {
    position: relative;
    background: var(--backdrop);
    font-family: 'Montserrat', sans-serif;
    color: var(--ink);
  }
  .section-label {
    position: absolute;
    font-family: 'Montserrat', sans-serif;
    font-weight: 600;
    font-size: 17px;
    letter-spacing: 2px;
    color: var(--label);
  }
  .section-label--letterhead { left: 29px; top: 36px; }
  .section-label--signature { left: 465px; top: 166px; }

  /* Letterhead */
  .letterhead {
    position: absolute;
    left: 31px; top: 66px;
    width: 399px; height: 513px;
    background: var(--paper);
    box-shadow: 4px 5px 6px rgba(0,0,0,0.35);
    overflow: hidden;
  }
  .brand {
    position: absolute;
    display: flex; align-items: center; gap: 5px;
    font-family: 'Roboto', sans-serif;
    font-weight: 700;
    color: var(--brand-light);
    white-space: nowrap;
    line-height: 1;
  }
  .brand__mark { background: var(--brand-light); flex: none; }
  .letterhead .brand { left: 26px; top: 38px; font-size: 20px; }
  .letterhead .brand__mark { width: 10px; height: 10px; }

  .letterhead__address {
    position: absolute;
    right: 124px; top: 44px;
    text-align: right;
    font-family: 'Roboto', sans-serif;
    font-size: 7px; line-height: 10px;
  }
  .letterhead__divider {
    position: absolute; left: 279px; top: 37px;
    width: 1px; height: 35px; background: var(--ink);
  }
  .letterhead__contacts {
    position: absolute; left: 284px; top: 40px;
    list-style: none;
    font-family: 'Roboto', sans-serif;
    font-size: 7px; line-height: 10.5px;
  }
  .contact-item { display: flex; align-items: center; gap: 7px; }
  .contact-item svg { flex: none; }
  .accent { color: var(--brand-blue); }

  .watermark {
    position: absolute; left: 53px; top: 246px;
    font-family: 'Roboto', sans-serif; font-weight: 700;
    font-size: 56px; line-height: 1; color: var(--watermark);
    white-space: nowrap;
  }
  .recipient {
    position: absolute; left: 26px; top: 131px;
    font-weight: 700; font-size: 7.4px; line-height: 9px;
    letter-spacing: 0.8px;
  }
  .letter-body {
    position: absolute; left: 26px; top: 170px; width: 347px;
    font-size: 7.8px; line-height: 9.5px; letter-spacing: 0.45px;
    text-align: justify; font-weight: 500;
    hyphens: auto; -webkit-hyphens: auto;
  }
  .letter-body p { margin-bottom: 9.5px; }
  .signature {
    position: absolute; left: 25px; top: 364px;
    width: 124px; height: 16px;
    background: linear-gradient(90deg, rgba(40,40,40,0.18), rgba(40,40,40,0.06));
    border-radius: 8px;
  }
  .signer-title {
    position: absolute; left: 25px; top: 383px;
    font-size: 11px; font-weight: 500; letter-spacing: 1.2px;
  }
  .letterhead__website {
    position: absolute; left: 0; right: 0; top: 474px;
    text-align: center; color: var(--brand-blue);
    font-size: 12px; letter-spacing: 1.6px; font-weight: 500;
  }
  .footer-band {
    position: absolute; left: 0; right: 0; bottom: 0;
    display: flex; height: 14px;
  }
  .footer-band__blue { background: var(--brand-blue); }
  .footer-band__dark { background: var(--band-dark); flex: 1; }
  .letterhead .footer-band__blue { width: 288px; }

  /* Email signature */
  .email-signature {
    position: absolute; left: 466px; top: 203px;
    width: 703px; height: 245px;
    background: var(--paper);
    box-shadow: 4px 5px 6px rgba(0,0,0,0.35);
    overflow: hidden;
  }
  .email-signature .brand { left: 133px; top: 98px; font-size: 32px; gap: 7px; }
  .email-signature .brand__mark { width: 14px; height: 14px; }
  .email-signature__divider {
    position: absolute; left: 355px; top: 44px;
    width: 2px; height: 141px; background: var(--brand-blue);
  }
  .person {
    position: absolute; left: 389px; top: 33px;
    font-family: 'Roboto', sans-serif;
  }
  .person__name { font-size: 26px; font-weight: 500; line-height: 30px; }
  .person__role { font-size: 16px; color: var(--brand-blue); line-height: 18px; }
  .person__address { font-size: 15px; line-height: 19.5px; margin-top: 6px; }
  .person__contacts { list-style: none; margin-top: 6px; font-size: 15px; line-height: 21px; }
  .person__contacts .contact-item { gap: 14px; }
  .email-signature .footer-band { height: 12px; }
  .email-signature .footer-band__blue { width: 509px; }
</style>
</head>
<body>
  <h2 class="section-label section-label--letterhead">Latterhead</h2>
  <h2 class="section-label section-label--signature">Email Signature</h2>

  <article class="letterhead">
    <div class="brand"><span class="brand__mark"></span>Stonefield</div>

    <div class="letterhead__address">Your Address line<br>here, Melbourne 23560</div>
    <div class="letterhead__divider"></div>
    <ul class="letterhead__contacts">
      <li class="contact-item">
        <svg width="8" height="8" viewBox="0 0 24 24"><path fill="#1f56a8" d="M6.6 10.8a15 15 0 0 0 6.6 6.6l2.2-2.2a1 1 0 0 1 1-.25 11 11 0 0 0 3.6.6 1 1 0 0 1 1 1V20a1 1 0 0 1-1 1A17 17 0 0 1 3 4a1 1 0 0 1 1-1h3.5a1 1 0 0 1 1 1c0 1.25.2 2.450.6 3.6a1 1 0 0 1-.25 1z"/></svg>
        +00 123 456 78
      </li>
      <li class="contact-item">
        <svg width="8" height="8" viewBox="0 0 24 24"><rect x="2" y="5" width="20" height="14" fill="#1f56a8"/><path d="M2 5l10 8 10-8M2 19l7-7M22 19l-7-7" stroke="#f0f0f0" stroke-width="1.6" fill="none"/></svg>
        yourname@mailbox.com
      </li>
      <li class="contact-item">
        <svg width="8" height="8" viewBox="0 0 24 24" fill="none" stroke="#1f56a8" stroke-width="1.8"><circle cx="12" cy="12" r="10"/><ellipse cx="12" cy="12" rx="4.5" ry="10"/><path d="M2 12h20M4 7h16M4 17h16"/></svg>
        <span>www.<span class="accent">yourwebsite</span>.com</span>
      </li>
    </ul>

    <div class="watermark" aria-hidden="true">Stonefield</div>

    <div class="recipient">TO<br>Corin Vale<br>Rivermoor, Eastland</div>

    <div class="letter-body">
      <p>Lorem ipsum dolor sit amet, consectetur adipisicing elit, sed do eiusmod tempor incididunt ut labore et dolore magna aliqua. Ut enim ad minim veniam, quis nostrud exercitation ullamco laboris nisi ut aliquip ex ea commodo consequat. Duis aute irure dolor in reprehenderit</p>
      <p>in voluptate velit esse cillum dolore eu fugiat nulla pariatur. Excepteur sint occaecat cupidatat non proident, sunt in culpa qui officia deserunt mollit anim id est laborum. Sed ut perspiciatis unde omnis iste natus error sit voluptatem</p>
      <p>accusantium doloremque laudantium, totam rem aperiam, eaque ipsa quae ab illo inventore veritatis et quasi architecto beatae vitae dicta sunt explicabo. Nemo enim ipsam voluptatem quia voluptas sit aspernatur aut odit aut fugit, sed quia consequuntur magni dolores eos qui</p>
      <p>ratione voluptatem sequi nesciunt. Neque porro quisquam est, qui dolorem ipsum quia dolor sit amet, consectetur, adipisci velit, sed quia non numquam eius modiquaerat</p>
    </div>

    <div class="signature" role="img" aria-label="Handwritten signature of the company president"></div>
    <div class="signer-title">President</div>

    <div class="letterhead__website">www.yourwebsite.com</div>
    <div class="footer-band"><span class="footer-band__blue"></span><span class="footer-band__dark"></span></div>
  </article>

  <section class="email-signature">
    <div class="brand"><span class="brand__mark"></span>Stonefield</div>
    <div class="email-signature__divider"></div>
    <div class="person">
      <div class="person__name">Corin Vale</div>
      <div class="person__role">Manager</div>
      <div class="person__address">Your Address line<br>here, Melbourne 23560</div>
      <ul class="person__contacts">
        <li class="contact-item">
          <svg width="17" height="17" viewBox="0 0 24 24"><path fill="#1f56a8" d="M6.6 10.8a15 15 0 0 0 6.6 6.6l2.2-2.2a1 1 0 0 1 1-.25 11 11 0 0 0 3.6.6 1 1 0 0 1 1 1V20a1 1 0 0 1-1 1A17 17 0 0 1 3 4a1 1 0 0 1 1-1h3.5a1 1 0 0 1 1 1c0 1.25.2 2.45.6 3.6a1 1 0 0 1-.25 1z"/></svg>
          +00 123 456 78
        </li>
        <li class="contact-item">
          <svg width="17" height="17" viewBox="0 0 24 24"><rect x="2" y="5" width="20" height="14" fill="#1f56a8"/><path d="M2 5l10 8 10-8M2 19l7-7M22 19l-7-7" stroke="#f0f0f0" stroke-width="1.6" fill="none"/></svg>
          yourname@mailbox.com
        </li>
        <li class="contact-item">
          <svg width="17" height="17" viewBox="0 0 24 24" fill="none" stroke="#1f56a8" stroke-width="1.6"><circle cx="12" cy="12" r="10"/><ellipse cx="12" cy="12" rx="4.5" ry="10"/><path d="M2 12h20M4 7h16M4 17h16"/></svg>
          <span>www.<span class="accent">yourwebsite</span>.com</span>
        </li>
      </ul>
    </div>
    <div class="footer-band"><span class="footer-band__blue"></span><span class="footer-band__dark"></span></div>
  </section>
</body>
</html>
```